sydney wedding photography business needs a business card design

we need a business card design for a sydney based wedding photography and videography business. our business name is :golden hour photography and video. our target clients are 24-35 yrs female. our style is candid, organic, natural, dynamic. we are a team of young photographers and videographers, and help brides to create memories that they will cherish for the rest of their lives. the logo will be provided. we want an elegant design that reflects our style, and also want to give a great impression to our clients that we are one of the best studios in sydney and our brand means quality and premium service.

Target Market(s)

bride to be, 24-35 years old, living in sydney and surrunding areas

Industry/Entity Type

Wedding Photography

Contact Information for Business Card

address: 57 marrow lane, bexton nsw 2041
mobile: 0431872056
phone: (02) 9361 2748
info@goldenhourstudio.net.au
www.goldenhourstudio.net.au
facebook:goldenhourbridals
instagram:goldenhourbridals

Font styles to use
Serif
Sans Serif

Requirements
Nice to have
• maybe add my slogan"memories beyond eternity" if the layout looks good
Should not have
• no black color, not good idea for wedding biz card

```html
<!DOCTYPE html>
<html lang="en">
<head>
<meta charset="utf-8">
<title>Golden Hour Photography and Video – Business Card</title>
<link rel="stylesheet" href="https://fonts.googleapis.com/css2?family=Ubuntu:wght@400;500&family=Oswald:wght@400&display=swap">
<style>
  :root {
    --page: #ffffff;
    --card-blue: #1c3d69;
    --panel-navy: #0e2036;
    --panel-edge: #08192b;
    --gold: #c8961e;
    --gold-soft: #d4a63a;
  }
  * { margin: 0; padding: 0; box-sizing: border-box; }
  html, body {
    width: 1200px;
    height: 1200px;
    overflow: hidden;
    background: var(--page);
  }
  .canvas {
    position: relative;
    width: 1200px;
    height: 1200px;
  }
  .card {
    position: absolute;
    left: 168px;
    width: 829px;
    height: 473px;
    display: block;
  }
  .card--front { top: 72px; }
  .card--back { top: 626px; }

  .card-bg { fill: var(--card-blue); }
  .panel { fill: var(--panel-navy); }
  .panel-edge { fill: var(--panel-edge); }
  .gold-fill { fill: var(--gold); }
  .gold-stroke { fill: none; stroke: var(--gold); }

  .brand-name {
    font-family: "Ubuntu", sans-serif;
    font-weight: 500;
    font-size: 44px;
    fill: var(--gold);
  }
  .brand-tagline {
    font-family: "Ubuntu", sans-serif;
    font-weight: 500;
    font-size: 14px;
    letter-spacing: 8px;
    fill: var(--gold);
  }
  .web-address {
    font-family: "Ubuntu", sans-serif;
    font-size: 11px;
    fill: var(--gold-soft);
  }
  .person-name {
    font-family: "Oswald", sans-serif;
    font-size: 41px;
    letter-spacing: 14px;
    fill: var(--gold);
  }
  .person-role {
    font-family: "Ubuntu", sans-serif;
    font-size: 10.5px;
    letter-spacing: 2.6px;
    fill: var(--gold-soft);
  }
  .contact-line {
    font-family: "Ubuntu", sans-serif;
    font-size: 17px;
    fill: var(--gold-soft);
  }
</style>
</head>
<body>
<main class="canvas">

  <!-- Front of card -->
  <svg class="card card--front" viewBox="0 0 829 473" aria-label="Business card front">
    <rect class="card-bg" width="829" height="473"/>
    <rect class="panel web-band" x="0" y="327" width="415" height="67"/>
    <circle class="panel logo-disc" cx="413" cy="236" r="158"/>

    <text class="brand-name" x="413" y="243" text-anchor="middle">Golden Hour</text>
    <text class="brand-tagline" x="417" y="278" text-anchor="middle">PHOTOGRAPHY</text>

    <g class="dot-trail dot-trail--left">
      <circle class="gold-fill" cx="10" cy="363" r="1.5"/>
      <circle class="gold-fill" cx="31" cy="363" r="2"/>
      <circle class="gold-fill" cx="51" cy="363" r="2.8"/>
      <circle class="gold-fill" cx="72" cy="363" r="3.5"/>
      <circle class="gold-fill" cx="92" cy="363" r="4.3"/>
      <circle class="gold-fill" cx="113" cy="363" r="5.2"/>
    </g>
    <text class="web-address" x="133" y="367">www.goldenhourstudio.net.au</text>
    <g class="dot-trail dot-trail--right">
      <circle class="gold-fill" cx="301" cy="363" r="5.2"/>
      <circle class="gold-fill" cx="321" cy="363" r="4.3"/>
      <circle class="gold-fill" cx="342" cy="363" r="3.5"/>
      <circle class="gold-fill" cx="362" cy="363" r="2.8"/>
      <circle class="gold-fill" cx="382" cy="363" r="2"/>
      <circle class="gold-fill" cx="403" cy="363" r="1.5"/>
    </g>
  </svg>

  <!-- Back of card -->
  <svg class="card card--back" viewBox="0 0 829 473" aria-label="Business card back">
    <rect class="card-bg" width="829" height="473"/>

    <text class="person-name" x="12" y="43">NAME</text>
    <text class="person-role" x="10" y="71">PHOTOGRAPHER&amp;VEDIOGRAPHER</text>

    <path class="panel-edge" d="M0 87 H493 A183 183 0 0 1 493 453 H0 Z"/>
    <path class="panel" d="M0 87 H478 A183 183 0 0 1 478 453 H0 Z"/>

    <!-- location pin -->
    <g class="icon icon--pin" transform="translate(198 146)">
      <path class="gold-fill" d="M0 -24 C-10 -24 -16 -16 -16 -9 C-16 2 -4 12 0 22 C4 12 16 2 16 -9 C16 -16 10 -24 0 -24 Z"/>
      <circle fill="var(--panel-navy)" cx="0" cy="-9" r="6.5"/>
    </g>
    <text class="contact-line" x="248" y="139">57 marrow lane,</text>
    <text class="contact-line" x="252" y="163">bexton nsw 2041.</text>

    <!-- phone handset -->
    <g class="icon icon--phone" transform="translate(188 216)">
      <path class="gold-fill" d="M4 0 L11 0 L14 10 L9 14 C11 22 17 28 25 31 L29 26 L38 30 L38 37 C34 40 27 40 20 36 C10 30 3 21 1 12 C0 7 1 3 4 0 Z"/>
    </g>
    <text class="contact-line" x="254" y="229">mobile: 0431872056</text>
    <text class="contact-line" x="254" y="253">phone: (02) 9361 2748</text>

    <!-- envelope -->
    <g class="icon icon--mail" transform="translate(191 300)">
      <rect class="gold-fill" x="0" y="0" width="34" height="23"/>
      <path d="M1 1 L17 13 L33 1 M1 22 L13 11 M33 22 L21 11" fill="none" stroke="var(--panel-navy)" stroke-width="2"/>
    </g>
    <text class="contact-line" x="256" y="314">info@goldenhourstudio.net.au</text>

    <!-- globe -->
    <g class="icon icon--globe" transform="translate(211 385)">
      <circle class="gold-fill" r="18"/>
      <ellipse cx="0" cy="0" rx="8" ry="18" fill="none" stroke="var(--panel-navy)" stroke-width="2"/>
      <path d="M-18 0 H18 M-15 -9 H15 M-15 9 H15" fill="none" stroke="var(--panel-navy)" stroke-width="2"/>
    </g>
    <text class="contact-line" x="261" y="378">facebook:goldenhourbridals</text>
    <text class="contact-line" x="261" y="403">instagram:goldenhourbridals</text>
  </svg>

</main>
</body>
</html>
```